Visitenkarte für Ergotherapiepraxis
Zielgruppe
Wir arbeiten mit Kindern und Erwachsene jeden Alters.
Diese Personen kommen mit Beeinträchtigungen (körperlich, seelisch, schulisch) im täglichen Leben zu uns. Wir unterstützen unsere Patienten die Beeinträchtigungen zu verringern oder zu kompensieren und so den Alltag besser bewältigen zu können.
Aufgabenstellung
Ein Design was Kinder und Erwachsene anspricht, aber nicht zu verspielt wirkt. Es soll vertrauenserweckend sein. Eventuell sollte die Visitenkarte ein "aufgehendes oder erblühendes oder aufsteigendes" Element enthalten (=zu Beginn war die Beeinträchtigung dann steigt die Lebensqualität als Folge der Behandlung)
Daten vorn:
Ergotherapiepraxis

```html
<!DOCTYPE html>
<html lang="de">
<head>
<meta charset="utf-8">
<title>Visitenkarte Ergotherapie Praxis</title>
<link rel="stylesheet" href="https://fonts.googleapis.com/css2?family=Ubuntu:ital,wght@0,300;0,400;1,300;1,400&display=swap">
<style>
  :root {
    --orange: #ff6600;
    --white: #ffffff;
    --ink: #3a3a3a;
    --backdrop-light: #f2f2f2;
    --backdrop-dark: #dcdcdc;
  }
  * { box-sizing: border-box; margin: 0; padding: 0; }
  html, body { width: 1200px; height: 415px; overflow: hidden; }
  body {
    position: relative;
    font-family: "Ubuntu", sans-serif;
    background: radial-gradient(ellipse at center, var(--backdrop-light) 0%, var(--backdrop-dark) 100%);
  }
  .card {
    position: absolute;
    top: 52px;
    width: 527px;
    height: 300px;
    overflow: hidden;
  }
  .card--back { left: 65px; background: var(--orange); color: var(--white); }
  .card--front { left: 615px; background: var(--white); color: var(--ink); }

  .emblem {
    position: absolute;
    width: 186px;
    height: 176px;
    border-radius: 6px;
  }
  .card--back .emblem {
    left: 28px; top: 70px;
    background: linear-gradient(180deg, rgba(255,255,255,0.28), rgba(255,255,255,0.14));
  }
  .card--front .emblem {
    left: 30px; top: 48px;
    background: linear-gradient(180deg, rgba(255,102,0,0.22), rgba(255,102,0,0.1));
  }

  .role {
    position: absolute;
    left: 248px; top: 118px;
    font-weight: 300;
    line-height: 1;
  }
  .role__title { font-size: 27px; letter-spacing: 0.3px; }
  .role__subtitle { font-size: 29px; font-style: italic; margin-top: 10px; margin-left: 50px; }

  .practice {
    position: absolute;
    left: 285px; top: 50px;
    width: 212px;
    text-align: center;
    line-height: 1;
  }
  .practice__name { font-size: 28px; font-weight: 300; letter-spacing: 0.4px; }
  .practice__type { font-size: 25px; font-style: italic; font-weight: 400; margin-top: 9px; }
  .practice__owner { font-size: 18px; font-weight: 400; margin-top: 11px; letter-spacing: 0.3px; }

  .phone {
    position: absolute;
    left: 284px; top: 220px;
    font-size: 31px;
    font-weight: 400;
    color: var(--orange);
    letter-spacing: 0.3px;
  }
  .address-bar {
    position: absolute;
    left: 0; bottom: 0;
    width: 100%;
    height: 35px;
    background: var(--orange);
    color: var(--white);
    font-size: 19px;
    font-weight: 400;
    line-height: 35px;
    padding-left: 50px;
    white-space: pre;
    letter-spacing: 0.2px;
  }
</style>
</head>
<body>
  <section class="card card--back">
    <div class="emblem" role="img" aria-label="Praxis-Symbol: stilisierte Figur zwischen zwei Pfeilen, weiß"></div>
    <div class="role">
      <p class="role__title">BEHANDELNDER</p>
      <p class="role__subtitle">Therapeut</p>
    </div>
  </section>

  <section class="card card--front">
    <div class="emblem" role="img" aria-label="Praxis-Symbol: stilisierte Figur zwischen zwei Pfeilen, orange"></div>
    <div class="practice">
      <p class="practice__name">ERGOTHERAPIE</p>
      <p class="practice__type">Praxis</p>
      <p class="practice__owner">MARLENE FALK</p>
    </div>
    <p class="phone">033845/41758</p>
    <p class="address-bar">Am Lindenhang | Hof 4   14972 Wiesenau, OT Brück</p>
  </section>
</body>
</html>
```